Business Card Design Project

A polished, very professional looking business card. I think we want to keep it all grey. I've attached our old logo, and current mockup in which case we really like the font.

Target Market(s)

Target Market are Bride and Grooms and Wedding Coordinators. We are wedding photographers

Industry/Entity Type

Business

Font styles to use
Serif
Sans Serif

Requirements
Must have
• An elegant, yet simple and sophisticated appearance.

Phone number, Email, Website and Social Media link.
Nice to have
• An element that can be spot glossed when printed. Not necessary though.
Should not have
• Bright colors, images or intensive graphics.

```html
<!DOCTYPE html>
<html lang="en">
<head>
<meta charset="utf-8">
<title>Carter Wells Photographers — Business Card</title>
<link rel="stylesheet" href="https://fonts.googleapis.com/css2?family=Raleway:wght@400;500&family=Open+Sans:wght@400&display=swap">
<style>
  :root {
    --backdrop: #3a322d;
    --card: #141414;
    --card-edge: #0c0c0c;
    --mark: #5a5a5a;
    --name: #5f5f5f;
    --tagline: #6c6c6c;
    --rule: #4a4a4a;
    --contact: #e6e6e6;
  }
  * { box-sizing: border-box; margin: 0; padding: 0; }
  html, body {
    width: 1200px; height: 716px; overflow: hidden;
    background: var(--backdrop);
  }
  .canvas {
    position: relative; width: 1200px; height: 716px;
    display: flex; align-items: center; justify-content: center; gap: 50px;
  }
  .card {
    position: relative;
    width: 525px; height: 300px;
    background: var(--card);
    border: 1px solid var(--card-edge);
    box-shadow: 0 8px 24px rgba(0,0,0,.45);
  }
  .brand {
    position: absolute;
    display: flex; flex-direction: column; align-items: center;
  }
  .card--front .brand { left: 50%; top: 50%; transform: translate(-50%, -50%); }
  .card--back .brand { left: 150px; top: 50%; transform: translate(-50%, -50%); }
  .brand__square {
    width: 46px; height: 46px;
    background: var(--mark);
    margin-bottom: 12px;
  }
  .brand__rule {
    width: 26px; height: 1px; background: var(--rule); margin-bottom: 8px;
  }
  .brand__name {
    font-family: "Raleway", sans-serif; font-weight: 400;
    font-size: 15px; letter-spacing: 4px; color: var(--name);
    text-transform: uppercase; white-space: nowrap;
  }
  .brand__tagline {
    font-family: "Raleway", sans-serif; font-weight: 500;
    font-size: 8px; letter-spacing: 5px; color: var(--tagline);
    text-transform: uppercase; margin-top: 4px;
  }
  .contact {
    position: absolute; left: 290px; top: 175px;
    list-style: none;
    font-family: "Open Sans", sans-serif; font-size: 13px;
    letter-spacing: 1.2px; color: var(--contact);
  }
  .contact li { display: flex; align-items: center; gap: 7px; line-height: 18px; }
  .contact svg { width: 10px; height: 10px; flex: none; }
  .contact .social { margin-top: 4px; }
</style>
</head>
<body>
<main class="canvas">
  <section class="card card--front" aria-label="Card front">
    <div class="brand">
      <div class="brand__square"></div>
      <div class="brand__rule"></div>
      <div class="brand__name">Carter Wells</div>
      <div class="brand__tagline">Photographers</div>
    </div>
  </section>

  <section class="card card--back" aria-label="Card back">
    <div class="brand">
      <div class="brand__square"></div>
      <div class="brand__rule"></div>
      <div class="brand__name">Carter Wells</div>
      <div class="brand__tagline">Photographers</div>
    </div>
    <ul class="contact">
      <li>
        <svg viewBox="0 0 10 10" aria-hidden="true"><rect x="2.5" y="0.5" width="5" height="9" rx="1" fill="none" stroke="#e6e6e6"/><circle cx="5" cy="8" r=".6" fill="#e6e6e6"/></svg>
        555.014.2290
      </li>
      <li>
        <svg viewBox="0 0 10 10" aria-hidden="true"><rect x="0.5" y="2" width="9" height="6" fill="none" stroke="#e6e6e6"/><path d="M.5 2 5 5.5 9.5 2" fill="none" stroke="#e6e6e6"/></svg>
        carter@carterwells.com
      </li>
      <li>
        <svg viewBox="0 0 10 10" aria-hidden="true"><circle cx="5" cy="5" r="4.3" fill="none" stroke="#e6e6e6"/><path d="M.7 5h8.6M5 .7c-2.4 2.4-2.4 6.2 0 8.6M5 .7c2.4 2.4 2.4 6.2 0 8.6" fill="none" stroke="#e6e6e6" stroke-width=".7"/></svg>
        www.carterwells.com
      </li>
      <li class="social">
        <svg viewBox="0 0 10 10" aria-hidden="true"><rect x="0.5" y="0.5" width="9" height="9" rx="1.5" fill="#e6e6e6"/></svg>
        @carterwells
      </li>
    </ul>
  </section>
</main>
</body>
</html>
```